Single-sided business card for restaurant bellwether with new logo made on this site

Business card options with new logo including restaurant name, address, phone number and website. This business card is single-sided only and will be presented at the hostess desk for clients to take. I would like to see options based on a cream card background, a white card background, a yellow card background and a burgundy colored background. It needs to be elegant and traditional.

Target Market(s)

local and international crowd

Industry/Entity Type

restaurant

Contact Information for Business Card

address, website and phone number

Font styles to use
Serif

Colors
EE7325
F08F49
F5BC92
FAE3D3
FDF4ED

Requirements
Must have
• new logo, address, phone number, website
Should not have
• more than three colors

```html
<!DOCTYPE html>
<html lang="es">
<head>
<meta charset="utf-8">
<title>Bellwether – Tarjeta de presentación</title>
<link href="https://fonts.googleapis.com/css2?family=Cinzel:wght@400&family=Gelasio:wght@400;700&display=swap" rel="stylesheet">
<style>
  :root {
    --stage: #e3e3e3;
    --card-top: #f8c245;
    --card-bottom: #f5b02c;
    --ink: #3b1c1f;
    --band: #34181b;
    --accent: #f7b733;
  }
  html, body {
    margin: 0;
    width: 1200px;
    height: 940px;
    overflow: hidden;
    background: var(--stage);
  }
  .card {
    position: absolute;
    left: 100px;
    top: 185px;
    width: 1000px;
    height: 571px;
    border-radius: 35px;
    overflow: hidden;
    background: linear-gradient(180deg, var(--card-top), var(--card-bottom));
    color: var(--ink);
    font-family: "Gelasio", Georgia, serif;
  }
  .brand-mark {
    position: absolute;
    left: 208px;
    top: 112px;
    width: 162px;
    height: 162px;
    background: var(--ink);
  }
  .brand-name {
    position: absolute;
    left: 398px;
    top: 104px;
    margin: 0;
    font-family: "Cinzel", "Times New Roman", serif;
    font-weight: 400;
    font-size: 82px;
    line-height: 78px;
    letter-spacing: 14px;
    color: var(--ink);
  }
  .brand-name span { display: block; }
  .address {
    position: absolute;
    right: 501px;
    top: 330px;
    margin: 0;
    font-style: normal;
    text-align: right;
    font-size: 26px;
    line-height: 32px;
  }
  .address strong { font-weight: 700; }
  .divider {
    position: absolute;
    left: 524px;
    top: 342px;
    width: 2px;
    height: 80px;
    background: var(--ink);
  }
  .reservations {
    position: absolute;
    left: 545px;
    top: 334px;
  }
  .reservations-label {
    margin: 0;
    font-weight: 700;
    font-size: 35px;
    line-height: 42px;
  }
  .reservations-phone {
    display: flex;
    align-items: center;
    gap: 6px;
    margin: 0;
    font-size: 46px;
    line-height: 52px;
  }
  .phone-icon { width: 36px; height: 36px; }
  .bottom-band {
    position: absolute;
    left: 0;
    top: 0;
    width: 1000px;
    height: 571px;
  }
  .website {
    position: absolute;
    right: 71px;
    top: 512px;
    margin: 0;
    font-weight: 700;
    font-size: 26px;
    color: var(--accent);
  }
</style>
</head>
<body>
  <section class="card" aria-label="Tarjeta de presentación Bellwether">
    <div class="brand-mark"></div>
    <h1 class="brand-name"><span>BELL</span><span>WETHER</span></h1>

    <address class="address">
      <strong>Restaurant Bellwether</strong><br>
      Jacaranda 415, Bahías de Huatulco<br>
      Oaxaca CP 70989
    </address>

    <div class="divider"></div>

    <div class="reservations">
      <p class="reservations-label">Reservaciones</p>
      <p class="reservations-phone">
        <svg class="phone-icon" viewBox="0 0 24 24" fill="none" stroke="currentColor" stroke-width="1.6" stroke-linejoin="round" aria-hidden="true">
          <path d="M5 3.5 8.2 3l2 4.6-2.3 1.6a11 11 0 0 0 6.9 6.9l1.6-2.3 4.6 2-.5 3.2A2 2 0 0 1 18.5 20 15.5 15.5 0 0 1 4 5.5 2 2 0 0 1 5 3.5Z"/>
          <path d="M14 3.5a6.5 6.5 0 0 1 6.5 6.5M14 6.8a3.2 3.2 0 0 1 3.2 3.2"/>
        </svg>
        958-412-3076
      </p>
    </div>

    <svg class="bottom-band" viewBox="0 0 1000 571" aria-hidden="true">
      <path fill="var(--band)" d="M0 488 C90 530 180 552 290 548 C450 542 650 470 830 464 C920 461 970 478 1000 497 L1000 571 L0 571 Z"/>
    </svg>

    <p class="website">www.Bellwether.com.mx</p>
  </section>
</body>
</html>
```